Verdant Holdings Scholarship

Looking to make an attractive scholarship description graphic for my website. Please use the text on the word doc and integrate the two graphics into the layout. Here's what I am looking to replace with the winning design: https://qmeadowllc.example/scholarship-contest/

Thank you

```html
<!DOCTYPE html>
<html lang="en">
<head>
<meta charset="utf-8">
<title>Verdant Holdings Scholarship</title>
<link rel="stylesheet" href="https://fonts.googleapis.com/css2?family=Open+Sans:wght@400;600;700&display=swap">
<style>
  :root {
    --purple: #5b2d86;
    --purple-band: #5a2f82;
    --gold: #c9a227;
    --ink: #1f1f1f;
    --white: #ffffff;
    --sky-top: #8fb6dc;
    --sky-bottom: #dfe9f3;
  }
  * { box-sizing: border-box; margin: 0; padding: 0; }
  html, body { width: 800px; height: 1200px; overflow: hidden; background: var(--white); }
  body { font-family: "Open Sans", Arial, sans-serif; color: var(--ink); }
  .page { position: relative; width: 800px; height: 1200px; overflow: hidden; background: var(--white); }

  .brand { position: absolute; top: 34px; left: 0; width: 800px; text-align: center;
    font-size: 22px; font-weight: 700; color: var(--purple); letter-spacing: 0.3px; }
  .brand-mark { display: inline-block; width: 14px; height: 14px; background: var(--gold); margin-right: 8px; vertical-align: 1px; }

  .main-nav { position: absolute; top: 112px; left: 0; width: 800px; display: flex; justify-content: center; gap: 24px;
    font-size: 11px; color: var(--ink); }
  .main-nav .active { color: var(--gold); }

  .hero { position: absolute; top: 141px; left: 0; width: 800px; height: 252px;
    background: linear-gradient(180deg, var(--sky-top) 0%, var(--sky-bottom) 100%); }
  .hero-arrow { position: absolute; top: 110px; }
  .hero-arrow.prev { left: 44px; }
  .hero-arrow.next { right: 44px; }

  .quote-band { position: absolute; top: 350px; left: 0; width: 800px; height: 43px; background: var(--purple-band);
    color: var(--white); text-align: center; font-size: 10.5px; line-height: 14px; padding-top: 7px; }
  .quote-band cite { font-style: normal; font-weight: 700; display: block; }

  .block { position: absolute; }
  .block-head { display: flex; align-items: center; gap: 14px; }
  .block-head svg { flex: none; }
  .block-title { font-size: 14.5px; font-weight: 700; line-height: 18px; color: var(--ink); }
  .block-text { font-size: 11.5px; line-height: 15px; margin-top: 10px; }
  .bullets { list-style: none; font-size: 11.5px; line-height: 15px; margin-top: 10px; }
  .bullets li { position: relative; padding-left: 16px; margin-bottom: 1px; }
  .bullets li::before { content: "•"; position: absolute; left: 2px; }
  .bullets.inset li { padding-left: 22px; }
  .bullets.inset li::before { left: 8px; }

  .footer-band { position: absolute; left: 0; bottom: 0; width: 800px; height: 14px; background: var(--purple-band); }
</style>
</head>
<body>
<div class="page">
  <div class="brand"><span class="brand-mark"></span>Verdant Holdings</div>

  <nav class="main-nav">
    <span class="active">Home</span><span>About Us</span><span>Rental Properties</span><span>Scholarship contest</span><span>Partners</span><span>Media</span><span>Contact Us</span>
  </nav>

  <div class="hero" role="img" aria-label="Photo of graduation caps and diplomas tossed into a blue sky">
    <svg class="hero-arrow prev" width="14" height="22" viewBox="0 0 14 22"><path d="M12 2 3 11l9 9" fill="none" stroke="#fff" stroke-width="2.5"/></svg>
    <svg class="hero-arrow next" width="14" height="22" viewBox="0 0 14 22"><path d="M2 2l9 9-9 9" fill="none" stroke="#fff" stroke-width="2.5"/></svg>
  </div>

  <div class="quote-band">
    "True scholarship consists in knowing not what things exist, but what they mean; it is not memory but judgment."
    <cite>- Edwin Marsh Caldwell.</cite>
  </div>

  <!-- Left column -->
  <section class="block" style="top:418px;left:82px;width:310px;">
    <div class="block-head">
      <svg width="42" height="42" viewBox="0 0 42 42" fill="none" stroke="var(--purple)" stroke-width="3">
        <circle cx="21" cy="21" r="18"/><circle cx="21" cy="21" r="11"/><circle cx="21" cy="21" r="4" fill="var(--purple)"/>
        <path d="M21 21 36 6M31 5h6v6"/>
      </svg>
      <h2 class="block-title">Purpose of this<br>Scholarship:</h2>
    </div>
    <ul class="bullets">
      <li>To increase trade school, college, and university opportunities of high school seniors</li>
      <li>To encourage high academic achievement in our youth</li>
      <li>To reward hard-working high school seniors and assist in collegiate expenses</li>
    </ul>
  </section>

  <section class="block" style="top:606px;left:82px;width:310px;">
    <div class="block-head">
      <svg width="42" height="46" viewBox="0 0 42 46" fill="none" stroke="var(--purple)" stroke-width="2.6">
        <rect x="3" y="6" width="28" height="37" rx="2"/><rect x="11" y="2" width="12" height="7" rx="1" fill="var(--purple)"/>
        <path d="M8 18h16M8 25h12M8 32h8"/><circle cx="32" cy="34" r="8" fill="#fff"/><path d="M28 34l3 3 5-6"/>
      </svg>
      <h2 class="block-title">Eligibility and Requirements at<br>the time of submission for this<br>scholarship:</h2>
    </div>
    <ul class="bullets inset">
      <li>Applicant must be an enrolled high school student in his/her senior year</li>
      <li>Applicant must be in good standing with their high school</li>
      <li>Applicant must have a cumulative grade point average of at least 2.5 on a 4.0 scale</li>
      <li>Applicant must be accepted to a 4-year accredited college, university, trade school or community college</li>
    </ul>
  </section>

  <section class="block" style="top:836px;left:82px;width:320px;">
    <div class="block-head">
      <svg width="42" height="46" viewBox="0 0 42 46" fill="none" stroke="var(--purple)" stroke-width="2.6">
        <rect x="3" y="2" width="22" height="40" rx="3"/><path d="M11 37h6"/>
        <circle cx="29" cy="27" r="7" fill="#fff"/><circle cx="29" cy="27" r="2.5"/>
        <path d="M29 17v3M29 34v3M19 27h3M36 27h3M22 20l2 2M34 32l2 2M22 34l2-2M34 22l2-2"/>
      </svg>
      <h2 class="block-title">Application:</h2>
    </div>
    <ul class="bullets" style="margin-top:18px;">
      <li>The application can be submitted via upload on this website, mail (see mailing address below), or scan &amp; email. Email address: danameadow@qmeadowllc.example. The Application package must include:</li>
      <li>Completed application form</li>
      <li>1 completed scholarship recommendation (teacher, guidance counselor, coach, employer, clergy, NOT friends or family)</li>
      <li>1 Essay no more than 2 pages in length, Times New Roman font (size 12), 1" margins, &amp; double-spaced</li>
      <li>Current high school transcript</li>
      <li>A copy of a College, University, Trade School or Community College acceptance letter</li>
    </ul>
  </section>

  <!-- Right column -->
  <section class="block" style="top:418px;left:442px;width:316px;">
    <div class="block-head">
      <svg width="36" height="44" viewBox="0 0 36 44" fill="none" stroke="var(--purple)" stroke-width="2.6">
        <rect x="3" y="5" width="30" height="37" rx="2"/><rect x="11" y="1" width="14" height="7" rx="1" fill="var(--purple)"/>
        <rect x="8" y="15" width="7" height="7"/><path d="M19 18h9"/><rect x="8" y="28" width="7" height="7"/><path d="M19 31h9"/>
      </svg>
      <h2 class="block-title">Scoring:</h2>
    </div>
    <p class="block-text" style="margin-top:12px;">The Verdant Holdings Scholarship Scoring Committee will evaluate each application and select ONE winner. If there is a tie, the prize money will be split. The winning essay will be scored based on the grading rubric (Rubric is in downloadable scholarship application packet).</p>
  </section>

  <section class="block" style="top:606px;left:442px;width:316px;">
    <div class="block-head">
      <svg width="38" height="48" viewBox="0 0 38 48" fill="none" stroke="var(--purple)" stroke-width="2.6">
        <path d="M19 2 4 9l15 7 15-7z" fill="var(--purple)"/><path d="M31 10v7"/>
        <circle cx="19" cy="32" r="13"/>
        <path d="M23 27c-1-2-3-2-4-2-3 0-4 2-4 3 0 4 8 2 8 6 0 2-2 3-4 3s-4-1-4-3M19 22v3M19 38v3"/>
      </svg>
      <h2 class="block-title">Scholarship Amount:</h2>
    </div>
    <p class="block-text" style="margin-top:20px;">The Verdant Holdings Scholarship will award a minimum of $1,500.00 to the winning applicant. Payment will be to the institution that the winner will attend in the fall.</p>
  </section>

  <section class="block" style="top:768px;left:442px;width:316px;">
    <div class="block-head">
      <svg width="44" height="46" viewBox="0 0 44 46" fill="none" stroke="var(--purple)" stroke-width="2.6">
        <rect x="3" y="5" width="30" height="37" rx="2"/><rect x="11" y="1" width="14" height="7" rx="1" fill="var(--purple)"/>
        <path d="M8 16h4M15 16h12M8 23h4M15 23h10M8 30h4"/>
        <circle cx="33" cy="35" r="9" fill="#fff"/><path d="M33 30v5h4"/>
      </svg>
      <h2 class="block-title">Deadline:</h2>
    </div>
    <p class="block-text" style="margin-top:14px;">The contest begins on 1 March. Applications postmarked, uploaded, and emailed after 31 May will not be accepted and returned to sender. Verdant Holdings will announce the winner no later than 1 August.</p>
  </section>

  <section class="block" style="top:940px;left:442px;width:316px;">
    <div class="block-head">
      <svg width="38" height="38" viewBox="0 0 38 38" fill="none" stroke="var(--purple)" stroke-width="2.8">
        <path d="M5 4h28a2 2 0 0 1 2 2v20a2 2 0 0 1-2 2H16l-8 7v-7H5a2 2 0 0 1-2-2V6a2 2 0 0 1 2-2z"/>
        <path d="M11 13h16M11 19h12"/>
      </svg>
      <h2 class="block-title" style="margin-left:12px;">Essay Topic</h2>
    </div>
    <p class="block-text" style="margin-top:14px;">The essay topic is posted on the last day of February.</p>
  </section>

  <div class="footer-band"></div>
</div>
</body>
</html>
```